Plume & Crest Hair Extensions needs a business card

We need a business card designed for an online luxury hair extensions business called Plume & Crest, we already have a logo and need an innovative business card (2-sided preferably). The strap line for the brand is 'Luxury Hair At Every Touchpoint!'. The brand is a premium brand selling virgin hair extensions and the target market is the mid-affluent ethnic woman as such the design should reflect this. The brand logo is grey and can be sent when requested.

Target Market(s)

25 to 35 year mid-affluent ethnic woman (Afro-American, Mixed Race, Asian)

Industry/Entity Type

Hair

Colors

Designer to choose colors to be used in the design.

Requirements
Must have
• Business Name: Plume and Crest
Strapline: Luxury hair at every touchpoint!
Domain: ​www.plumeandcrest.example
Email: info@plumeandcrest.example
sales and enquiries
44 07500 xxxxxxx

Please use the grey main brand logo depicted in page 2 of the attached pdf document

```html
<!DOCTYPE html>
<html lang="en">
<head>
<meta charset="utf-8">
<title>Plume &amp; Crest — Business Card</title>
<link rel="stylesheet" href="https://fonts.googleapis.com/css2?family=Libre+Caslon+Text&family=Arimo:wght@400&display=swap">
<style>
  :root {
    --page: #e9eaec;
    --silver-light: #ffffff;
    --silver-mid: #e4e5e8;
    --silver-dark: #b9bbc0;
    --title-grey: #6d7078;
    --ink-blue: #1d3a78;
    --logo-grey: #7b7e86;
    --card-shadow: rgba(40, 44, 56, 0.22);
  }
  * { box-sizing: border-box; margin: 0; padding: 0; }
  html, body {
    width: 1200px; height: 900px; overflow: hidden;
    background: var(--page);
  }
  .canvas {
    position: relative; width: 1200px; height: 900px;
    display: flex; align-items: center; justify-content: center; gap: 60px;
  }
  .card {
    position: relative; width: 525px; height: 300px;
    border-radius: 4px; overflow: hidden;
    box-shadow: 0 14px 34px var(--card-shadow);
  }
  .card-sheen {
    position: absolute; inset: 0;
    background:
      radial-gradient(ellipse 55% 70% at 55% 55%, var(--silver-light) 0%, var(--silver-mid) 55%, var(--silver-dark) 100%);
  }
  .brand-title {
    position: absolute;
    font-family: "Libre Caslon Text", Georgia, serif;
    font-weight: 400; color: var(--title-grey);
    letter-spacing: 1px; white-space: nowrap;
  }
  .front .brand-title { top: 44px; right: 34px; font-size: 50px; }
  .strapline {
    position: absolute; top: 112px; right: 40px;
    font-family: "Arimo", Arial, sans-serif;
    font-size: 21px; color: var(--ink-blue); letter-spacing: 0.5px;
  }
  .logo-name {
    position: absolute; left: 22px; top: 128px;
    font-family: "Arimo", Arial, sans-serif;
    font-size: 13px; letter-spacing: 2px; text-transform: uppercase;
    color: var(--logo-grey);
  }
  .back .brand-title { top: 26px; left: 30px; font-size: 48px; }
  .contact-list {
    position: absolute; top: 104px; left: 56px;
    list-style: none;
    font-family: "Arimo", Arial, sans-serif;
    font-size: 17px; line-height: 1.42; color: var(--ink-blue);
  }
  .contact-list .indent { padding-left: 52px; }
  .back-url {
    position: absolute; bottom: 24px; left: 0; right: 0; text-align: center;
    font-family: "Arimo", Arial, sans-serif;
    font-size: 23px; color: var(--ink-blue); letter-spacing: 0.5px;
  }
</style>
</head>
<body>
<main class="canvas">
  <section class="card back" aria-label="Business card, contact side">
    <div class="card-sheen" role="img" aria-label="Silver radiant sheen with fine straight, wavy and curly hair strand pattern"></div>
    <h2 class="brand-title">Plume &amp; Crest</h2>
    <ul class="contact-list">
      <li>Business Name: Plume and Crest</li>
      <li>Website: www.plumeandcrest.example</li>
      <li>Email: info@plumeandcrest.example</li>
      <li class="indent">sales and enquiries</li>
      <li class="indent">44 07500 xxxxxxx</li>
    </ul>
    <p class="back-url">www.plumeandcrest.example</p>
  </section>

  <section class="card front" aria-label="Business card, brand side">
    <div class="card-sheen" role="img" aria-label="Silver radiant sheen with fine straight, wavy and curly hair strand pattern"></div>
    <p class="logo-name">Plume &amp; Crest</p>
    <h1 class="brand-title">Plume &amp; Crest</h1>
    <p class="strapline">Luxury hair at every touchpoint!</p>
  </section>
</main>
</body>
</html>
```